Business card for a "family office" company

Please provide professional looking business card designs, incorporating the attached logo and below details. Harrowmere Holdings Pty Ltd is a family office / financial investment company. We are looking for a modern, professional and contemporary card design.

Industry/Entity Type

Finance

Contact Information for Business Card

Name: Dean Mollick
Title: Director
Company: Harrowmere Holdings Pty Ltd
Email: harrowdean@quillnet.example
Mobile: 0462 735 418
Address: 4/312 Barnaby Parade, Fernhollow QX 7420, Australia

Requirements
Must have
• All details above and the logo. logo only on back side. incorporate colours of logo
Nice to have
• up to you
Should not have
• ?

```html
<!DOCTYPE html>
<html lang="en">
<head>
<meta charset="utf-8">
<title>Harrowmere Holdings – Business Card</title>
<link rel="stylesheet" href="https://fonts.googleapis.com/css2?family=Open+Sans:wght@400;600&display=swap">
<style>
  :root {
    --navy: #1f2266;
    --ink: #3a3a3a;
    --muted: #6b6b6b;
    --card: #f6f6f4;
    --backdrop: #d9d9d9;
    --rule: #4a4d80;
  }
  * { box-sizing: border-box; margin: 0; padding: 0; }
  html, body {
    width: 1200px; height: 1200px; overflow: hidden;
    background: var(--backdrop);
    font-family: "Open Sans", sans-serif;
  }
  .canvas { position: relative; width: 1200px; height: 1200px; }
  .card {
    position: absolute;
    width: 700px; height: 428px;
    background: var(--card);
    box-shadow: 0 2px 0 #e8e8e8, 0 4px 0 #dcdcdc, 0 10px 24px rgba(0,0,0,.18);
  }
  .card--back { left: 140px; top: 130px; display: flex; align-items: center; justify-content: center; }
  .card--front { left: 360px; top: 640px; display: flex; align-items: center; }

  .brand { display: flex; align-items: center; gap: 16px; }
  .brand__mark { width: 34px; height: 34px; background: var(--navy); flex: none; }
  .brand__name {
    color: var(--navy); font-weight: 600; letter-spacing: .08em;
    text-transform: uppercase; line-height: 1.1;
  }
  .card--back .brand__name { font-size: 34px; }
  .card--front .brand { width: 370px; justify-content: center; }
  .card--front .brand__name { font-size: 24px; }
  .card--front .brand__mark { width: 26px; height: 26px; }

  .divider { width: 1px; height: 250px; background: var(--rule); flex: none; }

  .details { padding-left: 30px; color: var(--ink); font-size: 14px; }
  .details__name { color: var(--navy); font-size: 24px; font-weight: 400; }
  .details__title { color: var(--muted); font-size: 13px; margin-bottom: 18px; }
  .details__company { color: var(--navy); font-size: 14px; margin-bottom: 10px; }
  .contact { list-style: none; }
  .contact li { display: flex; align-items: flex-start; gap: 10px; margin-bottom: 4px; line-height: 1.35; }
  .contact svg { width: 14px; height: 14px; flex: none; margin-top: 2px; fill: var(--ink); }
  .contact li.contact__address { margin-top: 10px; }
</style>
</head>
<body>
<div class="canvas">
  <section class="card card--back" aria-label="Card back">
    <div class="brand">
      <span class="brand__mark"></span>
      <span class="brand__name">Harrowmere<br>Holdings</span>
    </div>
  </section>

  <section class="card card--front" aria-label="Card front">
    <div class="brand">
      <span class="brand__mark"></span>
      <span class="brand__name">Harrowmere<br>Holdings</span>
    </div>
    <div class="divider"></div>
    <div class="details">
      <h1 class="details__name">Dean Mollick</h1>
      <p class="details__title">Director</p>
      <p class="details__company">Harrowmere Holdings Pty Ltd</p>
      <ul class="contact">
        <li>
          <svg viewBox="0 0 16 16" aria-hidden="true"><rect x="4" y="1" width="8" height="14" rx="1.5"/><rect x="5.5" y="3" width="5" height="8" fill="#f6f6f4"/></svg>
          <span>0462 735 418</span>
        </li>
        <li>
          <svg viewBox="0 0 16 16" aria-hidden="true"><path d="M1 3h14v10H1z"/><path d="M1 3l7 6 7-6" fill="none" stroke="#f6f6f4" stroke-width="1.3"/></svg>
          <span>harrowdean@quillnet.example</span>
        </li>
        <li class="contact__address">
          <svg viewBox="0 0 16 16" aria-hidden="true"><path d="M8 1a5 5 0 0 0-5 5c0 4 5 9 5 9s5-5 5-9a5 5 0 0 0-5-5z"/><circle cx="8" cy="6" r="2" fill="#f6f6f4"/></svg>
          <span>4/312 Barnaby Parade<br>Fernhollow QX 7420, Australia</span>
        </li>
      </ul>
    </div>
  </section>
</div>
</body>
</html>
```